Corin Abbott Business Cards

We Need two Business Cards with bleeds. the only difference between the two cards is the backaround color one lilac and pink. Attached we have the cards please match up the logo's and text. Take out the orange box out.

Target Market(s)

double-sided business cards

Industry/Entity Type

Business

Logo Text

match up as best as possible

Colors
f59195
d2a4cc

Requirements
Must have
• n/a
Nice to have
• n/a
Should not have
• n/a

```html
<!DOCTYPE html>
<html lang="en">
<head>
<meta charset="utf-8">
<title>Corin Abbott Business Cards</title>
<link rel="stylesheet" href="https://fonts.googleapis.com/css2?family=Source+Sans+3:wght@400;600;700&display=swap">
<style>
  :root {
    --stage: #efe9e4;
    --card-pink: #de8c96;
    --card-lilac: #d3a3cb;
    --mark: #7b1e32;
    --ink: #231f20;
  }
  * { box-sizing: border-box; margin: 0; padding: 0; }
  html, body {
    width: 1200px;
    height: 1000px;
    overflow: hidden;
    background: var(--stage);
    font-family: "Source Sans 3", "Myriad Pro", sans-serif;
  }
  .sheet {
    position: relative;
    width: 1200px;
    height: 1000px;
  }
  .card {
    position: absolute;
    left: 280px;
    width: 640px;
    height: 350px;
    overflow: hidden;
    box-shadow: 0 3px 10px rgba(0, 0, 0, 0.18);
    color: var(--ink);
  }
  .card--pink  { top: 110px; background: var(--card-pink); }
  .card--lilac { top: 540px; background: var(--card-lilac); }

  .brand {
    position: absolute;
    left: 40px;
    top: 0;
    bottom: 0;
    width: 160px;
    display: flex;
    align-items: center;
    gap: 10px;
    color: var(--mark);
    font-weight: 700;
    font-size: 26px;
    line-height: 1.05;
  }
  .brand__dot {
    flex: none;
    width: 24px;
    height: 24px;
    border: 4px solid var(--mark);
    border-radius: 50%;
  }

  .header {
    position: absolute;
    right: 38px;
    top: 28px;
    text-align: right;
  }
  .header__name {
    font-weight: 700;
    font-size: 28px;
    line-height: 1;
    margin-bottom: 14px;
  }
  .header__line {
    font-size: 21px;
    line-height: 1.4;
  }
  .header__note {
    font-size: 16.5px;
    margin-top: 4px;
  }

  .services, .contact {
    position: absolute;
    top: 186px;
    font-size: 17px;
    line-height: 27px;
    list-style: none;
  }
  .services {
    left: 213px;
    color: var(--mark);
  }
  .contact {
    right: 38px;
    text-align: right;
  }
</style>
</head>
<body>
<main class="sheet">

  <section class="card card--pink" aria-label="Business card, pink">
    <div class="brand"><span class="brand__dot"></span><span>Wren<br>Care</span></div>
    <header class="header">
      <h1 class="header__name">Corin Abbott-Halvey, MD</h1>
      <p class="header__line">Board Certified</p>
      <p class="header__line">Women`s Health &amp; Wellness Specialist</p>
      <p class="header__note">By Appointment</p>
    </header>
    <ul class="services">
      <li>Obstetrics</li>
      <li>Gynecology</li>
      <li>Family Planning</li>
      <li>Menopause</li>
    </ul>
    <ul class="contact">
      <li>418 Birchwood Lane,</li>
      <li>Fairhaven NY 11090</li>
      <li>PH: 555.201.3418/3419</li>
      <li>FX: 555.201.3453</li>
      <li>Email: c-halvey@inboxmail.net</li>
    </ul>
  </section>

  <section class="card card--lilac" aria-label="Business card, lilac">
    <div class="brand"><span class="brand__dot"></span><span>Wren<br>Care</span></div>
    <header class="header">
      <h1 class="header__name">Corin Abbott-Halvey, MD</h1>
      <p class="header__line">Board Certified</p>
      <p class="header__line">Women`s Health &amp; Wellness Specialist</p>
      <p class="header__note">By Appointment</p>
    </header>
    <ul class="services">
      <li>Obstetrics</li>
      <li>Gynecology</li>
      <li>Family Planning</li>
      <li>Weight Managment</li>
      <li>Menopause</li>
    </ul>
    <ul class="contact">
      <li>88-24 Meadowbrook Parkway</li>
      <li>Meadowbrook, New York 11490</li>
      <li>PH: 555.318.4125</li>
      <li>FX: 555.318.4126</li>
      <li>Email: c-halvey@inboxmail.net</li>
    </ul>
  </section>

</main>
</body>
</html>
```